Australian small vineyard seeking wine label.

We need a wine label design for a new wine brand \Boutique winery - 2 vintages so far, looking for something a little eye catching, but simple.
Wine label name: Brent and Co
2013 Cabernet Shiraz
2014 Shiraz
Estate grown
Vineyard located at Sevenhill in the Clare valley South Australia.

Target Market(s)

ladies aged between 20 and 50

Industry/Entity Type

Boutique

Logo Text

Brent and Co

Logo styles of interest
Emblem Logo
Pictorial/Combination Logo
Abstract Logo
Character Logo
Font styles to use
Serif
Script

Requirements
Must have
• easy to read text
Nice to have
• The grape grower and winemaker is Martin Brent -
• had some thoughts of Captain Brent - Australian - naval flag
• But very open to ideas
Should not have
• over complications and colors due to cost of wine label being determined by amount of colors required abd print set up.

```html
<!DOCTYPE html>
<html lang="en">
<head>
<meta charset="utf-8">
<title>Brent and Co Shiraz 2014 Label</title>
<link rel="stylesheet" href="https://fonts.googleapis.com/css2?family=Cinzel:wght@400&family=Cormorant+SC:wght@500&display=swap">
<style>
  :root {
    --backdrop: #d9d9d9;
    --cream: #ece6d0;
    --label-black: #1d1d1d;
    --ink: #151515;
    --chalk: #e8e8e6;
    --chalk-soft: #c9c9c6;
  }
  * { box-sizing: border-box; margin: 0; padding: 0; }
  html, body {
    width: 1200px; height: 800px; overflow: hidden;
    background: var(--backdrop);
  }
  .canvas {
    width: 1200px; height: 800px;
    display: flex; align-items: center; justify-content: center;
  }
  .label {
    width: 620px;
    box-shadow: 0 6px 24px rgba(0,0,0,0.18);
  }
  .label__band {
    height: 96px;
    background: var(--cream);
    display: flex; align-items: center; justify-content: center;
  }
  .label__brand {
    font-family: "Cormorant SC", serif;
    font-weight: 500;
    font-size: 44px;
    letter-spacing: 3px;
    color: var(--ink);
  }
  .label__panel {
    background: var(--label-black);
    padding: 44px 40px 40px;
    display: flex; flex-direction: column; align-items: center;
    color: var(--chalk);
  }
  .label__ship {
    width: 170px; height: 150px;
  }
  .label__variety {
    font-family: "Cinzel", serif;
    font-weight: 400;
    font-size: 46px;
    letter-spacing: 9px;
    margin-top: 18px;
  }
  .label__vintage {
    font-family: "Cormorant SC", serif;
    font-weight: 500;
    font-size: 22px;
    letter-spacing: 2px;
    margin-top: 10px;
  }
  .label__estate {
    font-family: "Cormorant SC", serif;
    font-weight: 500;
    font-size: 21px;
    letter-spacing: 1px;
    margin-top: 30px;
    color: var(--chalk-soft);
  }
  .label__origin {
    font-family: "Cormorant SC", serif;
    font-weight: 500;
    font-size: 19px;
    letter-spacing: 1.5px;
    margin-top: 26px;
    color: var(--chalk-soft);
  }
</style>
</head>
<body>
<main class="canvas">
  <article class="label">
    <header class="label__band">
      <h1 class="label__brand">Brent and Co</h1>
    </header>
    <section class="label__panel">
      <svg class="label__ship" viewBox="0 0 170 150" role="img" aria-label="Pen-and-ink illustration of a three-masted sailing ship on the waves">
        <defs>
          <radialGradient id="ship-tone" cx="50%" cy="50%" r="60%">
            <stop offset="0%" stop-color="#8a8a88"/>
            <stop offset="100%" stop-color="#1d1d1d"/>
          </radialGradient>
        </defs>
        <rect width="170" height="150" fill="url(#ship-tone)"/>
      </svg>
      <h2 class="label__variety">SHIRAZ</h2>
      <p class="label__vintage">2014</p>
      <p class="label__estate">Estate Grown</p>
      <p class="label__origin">Ridgefield&nbsp; Marlow Valley South Australia</p>
    </section>
  </article>
</main>
</body>
</html>
```